Web Design for ROLV Air conditioning company

Hello,

I am calling on you for the modernization of the company's website
https://clarovent-services-techniques.fr/

The new one must include the new logo with the new graphic charter (color, style ...)

I'm looking for a simple design (less is more), a font written without Serif, the logo that brings a touch of color and modernity.

(maintenance and installation company for air conditioning and ventilation systems)
COLORS: in line with the logo

CHAPTER:

# PRESENTATION
# SERVICES
AIR CONDITIONING (ice cube icon)
HEATING (flame icon)
AIR TREATMENT (icon fan)
# ACHIEVEMENTS

# CONTACT
CONTACT FORM
GOOGLE MAPS

Target Market(s)

Showcase site for our customers

Coding

Coded - Design and coding required

Number of Pages Required

4 page

Font styles to use
Sans Serif

Colors
33b8a4
33a6d7
3176b5
ffffff

Requirements
Must have
• Clear and fluid navigation
a visual identity of the page with the logo
Should not have
• Overloaded.

```html
<!DOCTYPE html>
<html lang="en">
<head>
<meta charset="utf-8">
<title>ROLV – Clarovent Services Techniques</title>
<link rel="stylesheet" href="https://fonts.googleapis.com/css2?family=Montserrat:wght@400;500;600;700;800&display=swap">
<style>
:root{
  --teal:#33b8a4;
  --green:#3cc98b;
  --blue:#33a6d7;
  --navy:#1e3b7a;
  --deep:#1f3a4a;
  --slate:#2e3d49;
  --link:#2a9bc4;
  --text:#4a4a4a;
  --white:#ffffff;
  --grad:linear-gradient(90deg,#2a8fc4 0%,#3cc98b 100%);
}
*{box-sizing:border-box;margin:0;padding:0}
html,body{width:1200px;height:3276px;overflow:hidden;background:var(--white);font-family:'Montserrat',sans-serif;color:var(--text)}
.page{position:relative;width:1200px;height:3276px}
.abs{position:absolute}

/* header */
.site-header{position:absolute;top:0;left:0;width:1200px;height:90px;background:var(--white)}
.brand{position:absolute;left:66px;top:22px;display:flex;align-items:flex-end;gap:12px}
.brand-mark{display:flex;align-items:center;gap:8px;font-weight:800;font-size:40px;line-height:1;color:var(--deep);letter-spacing:1px}
.brand-mark i{display:block;width:12px;height:12px;background:var(--teal)}
.brand-tag{font-size:11px;font-weight:600;color:#6b7a86;padding-bottom:6px}
.main-nav{position:absolute;left:480px;top:36px;display:flex;gap:46px;font-size:14px;font-weight:700;color:var(--teal)}
.main-nav a{color:var(--teal);text-decoration:none;position:relative}
.main-nav a.active{color:var(--deep)}
.main-nav a.active::after{content:"";position:absolute;left:6px;right:6px;bottom:-10px;height:3px;background:var(--teal);border-radius:2px}
.header-phone{position:absolute;left:952px;top:34px;display:flex;gap:6px;align-items:center;font-weight:700;font-size:17px;color:var(--deep)}

/* hero */
.hero{position:absolute;top:90px;left:0;width:1200px;height:584px;overflow:hidden}
.hero-photo{position:absolute;inset:0;background:linear-gradient(90deg,#f6f6f6 0%,#eeeeee 35%,#d6d9de 60%,#a9b6cc 80%,#c9cdd4 100%)}
.hero-fade{position:absolute;inset:0;background:linear-gradient(90deg,rgba(255,255,255,.92) 0%,rgba(255,255,255,.7) 35%,rgba(255,255,255,0) 55%)}
.hero-title{position:absolute;left:106px;top:150px;font-size:35px;font-weight:800;line-height:1.15;color:var(--deep);letter-spacing:.5px}
.hero-text{position:absolute;left:106px;top:244px;width:370px;font-size:17px;line-height:1.6;color:#3e3e3e}
.btn{display:inline-flex;align-items:center;justify-content:center;border-radius:30px;background:var(--grad);color:var(--white);font-weight:700;text-transform:uppercase;text-decoration:none}
.hero .btn{position:absolute;left:106px;top:320px;width:224px;height:56px;font-size:16px}

/* about */
.about-frame{position:absolute;left:174px;top:840px;width:358px;height:298px;border:5px solid var(--green);border-top:none;border-left:none}
.about-frame::before{content:"";position:absolute;left:0;bottom:0;width:5px;height:40px;background:var(--green)}
.about-photo{position:absolute;left:113px;top:761px;width:383px;height:339px;background:linear-gradient(135deg,#d9dee2 0%,#eef1f3 45%,#c9cdd1 100%);box-shadow:0 10px 30px rgba(0,0,0,.18)}
.section-title{font-size:31px;font-weight:700;color:var(--deep);position:relative}
.section-title::after{content:"";position:absolute;left:0;bottom:-14px;width:70px;height:3px;background:var(--grad)}
.about-title{position:absolute;left:611px;top:788px}
.about-text{position:absolute;left:611px;top:860px;width:480px;font-size:17px;line-height:31px;color:#555}
.about .btn{position:absolute;left:611px;top:1054px;width:209px;height:52px;font-size:15px}

/* stats */
.stats{position:absolute;left:100px;top:1258px;width:980px;height:84px;display:flex}
.stat{text-align:center;border-right:3px solid #d6dbe0}
.stat:last-child{border-right:none}
.stat strong{display:block;font-size:48px;font-weight:800;color:var(--navy);line-height:1}
.stat span{display:block;margin-top:20px;font-size:19px;font-weight:500;color:var(--link)}

/* services */
.services{position:absolute;top:1366px;left:0;width:1200px;height:642px;background:linear-gradient(90deg,#3aa6c6 0%,#3cbfae 50%,#46cc8e 100%);overflow:hidden}
.services-bg{position:absolute;inset:0;background:linear-gradient(90deg,rgba(255,255,255,.12),rgba(255,255,255,0) 40%,rgba(255,255,255,.08))}
.services-title{position:absolute;top:140px;left:0;width:1200px;text-align:center;font-size:31px;font-weight:700;color:var(--white)}
.service{position:absolute;top:205px;width:322px;height:371px}
.service svg{position:absolute;inset:0}
.service-label{position:absolute;left:0;width:322px;top:206px;text-align:center;font-size:20px;font-weight:700;color:var(--white)}

/* appointment */
.appointment{position:absolute;top:2008px;left:0;width:1200px;height:560px;background:var(--slate)}
.appointment-photo{position:absolute;left:0;top:0;width:600px;height:560px;background:linear-gradient(180deg,#7e4c43 0%,#6f5049 50%,#5d6a58 75%,#6f9a3c 100%)}
.appointment-fade{position:absolute;left:400px;top:0;width:220px;height:560px;background:linear-gradient(90deg,rgba(46,61,73,0),var(--slate))}
.appointment-title{position:absolute;left:613px;top:80px;font-size:28px;font-weight:700;color:var(--white)}
.form-field{position:absolute;left:616px;width:457px;height:43px;border:1.5px solid #9eb0bd;font-size:12px;color:var(--white);padding:14px 20px}
.form-field.message{height:108px}
.appointment .btn{position:absolute;left:616px;top:429px;width:160px;height:48px;font-size:19px}

/* contact */
.contact-title{position:absolute;left:123px;top:2666px}
.contact-list{position:absolute;left:130px;top:2740px;list-style:none;font-size:16px;line-height:29px;color:#333}
.contact-list li{position:relative;padding-left:34px;margin-bottom:28px}
.contact-list li svg{position:absolute;left:0;top:5px}
.map{position:absolute;left:521px;top:2652px;width:570px;height:324px;background:linear-gradient(180deg,#eceeef 0%,#e3e6e8 100%)}

/* footer */
.site-footer{position:absolute;top:3083px;left:0;width:1200px;height:193px;background:var(--slate)}
.footer-nav{position:absolute;top:52px;left:0;width:1200px;display:flex;justify-content:center;gap:84px;font-size:16px;font-weight:700;color:var(--white)}
.footer-nav a{color:var(--white);text-decoration:none}
.copyright{position:absolute;top:92px;left:0;width:1200px;text-align:center;font-size:13px;color:#a9b4bc}
.social{position:absolute;top:131px;left:538px;display:flex;gap:6px}
.social span{display:block;width:32px;height:32px;border-radius:50%;border:1.5px solid var(--white)}
.social span:first-child{border-color:var(--teal)}
</style>
</head>
<body>
<div class="page">

  <header class="site-header">
    <div class="brand">
      <div class="brand-mark"><i></i>ROLV</div>
      <div class="brand-tag">CLAROVENT SERVICES TECHNIQUES</div>
    </div>
    <nav class="main-nav">
      <a class="active" href="#">HOME</a>
      <a href="#">ABOUT</a>
      <a href="#">SERVICES</a>
      <a href="#">CONTACT US</a>
    </nav>
    <div class="header-phone">
      <svg width="20" height="20" viewBox="0 0 24 24"><path fill="#2a9bc4" d="M6.6 10.8a15 15 0 0 0 6.6 6.6l2.2-2.2a1 1 0 0 1 1-.25 11.4 11.4 0 0 0 3.6.57 1 1 0 0 1 1 1V20a1 1 0 0 1-1 1A17 17 0 0 1 3 4a1 1 0 0 1 1-1h3.5a1 1 0 0 1 1 1c0 1.25.2 2.45.57 3.57a1 1 0 0 1-.25 1z"/></svg>
      987 654 3210
    </div>
  </header>

  <section class="hero">
    <div class="hero-photo" role="img" aria-label="Technician in blue overalls servicing a wall-mounted air conditioner while a client watches"></div>
    <div class="hero-fade"></div>
    <h1 class="hero-title">CLAROVENT SERVICES<br>TECHNIQUES LYON</h1>
    <p class="hero-text">Lorem ipsum dolor sit amet, consectetur adipiscing elit, sed do eiusmod tem</p>
    <a class="btn" href="#">Request a quote</a>
  </section>

  <section class="about">
    <div class="about-frame"></div>
    <div class="about-photo" role="img" aria-label="Outdoor air conditioning units installed beside a house"></div>
    <h2 class="section-title about-title">ABOUT ROLV</h2>
    <p class="about-text">Lorem ipsum dolor sit amet, consectetur adipiscing elit, sed do eiusmod tempor incididunt ut labore et dolore magna aliqua. Ut enim ad minim veniam, quis nostrud exercitation ullamco laboris nisi ut aliquip ex ea commodo consequat. Duis aute irure dolor</p>
    <a class="btn" href="#">Request a quote</a>
  </section>

  <div class="stats">
    <div class="stat" style="width:216px"><strong>07</strong><span>CLIENTS</span></div>
    <div class="stat" style="width:242px"><strong>650</strong><span>CONTRACT</span></div>
    <div class="stat" style="width:240px"><strong>590</strong><span>SATISFIED</span></div>
    <div class="stat" style="width:282px"><strong>1752</strong><span>STOCK PRODUCTS</span></div>
  </div>

  <section class="services">
    <div class="services-bg" role="img" aria-label="Faint background photo of a technician and air conditioning equipment"></div>
    <svg class="abs" style="left:0;top:0" width="1200" height="112" viewBox="0 0 1200 112">
      <polygon points="0,0 1200,0 1200,18 600,112 0,18" fill="#ffffff"/>
      <polygon points="0,0 600,94 1200,0 1200,18 600,112 0,18" fill="#2e3d49"/>
    </svg>
    <h2 class="services-title">OUR SERVICES</h2>

    <div class="service" style="left:97px">
      <svg width="322" height="371" viewBox="0 0 322 371" role="img" aria-label="Photo of an outdoor air conditioning unit">
        <polygon points="161,0 322,93 322,278 161,371 0,278 0,93" fill="#6e7368"/>
        <g fill="none" stroke="#fff" stroke-width="3">
          <rect x="151" y="115" width="28" height="28" rx="3"/>
          <rect x="132" y="143" width="28" height="28" rx="3"/>
          <rect x="162" y="143" width="28" height="28" rx="3"/>
          <line x1="125" y1="174" x2="197" y2="174"/>
        </g>
      </svg>
      <div class="service-label">AIR CONDITIONING</div>
    </div>

    <div class="service" style="left:442px">
      <svg width="322" height="371" viewBox="0 0 322 371" role="img" aria-label="Photo of a glowing gas heater">
        <polygon points="161,0 322,93 322,278 161,371 0,278 0,93" fill="#2a1f1c"/>
        <polygon points="161,0 322,93 322,278 161,371 0,278 0,93" fill="#c8621f" opacity=".35"/>
        <path d="M161 115c10 15 26 25 26 44a26 26 0 0 1-52 0c0-12 8-18 12-26 3 8 6 12 10 12 0-10 0-20 4-30z" fill="none" stroke="#fff" stroke-width="3"/>
        <path d="M161 150c6 7 12 12 12 19a12 12 0 0 1-24 0c0-7 6-11 12-19z" fill="none" stroke="#fff" stroke-width="3"/>
      </svg>
      <div class="service-label">HEATING</div>
    </div>

    <div class="service" style="left:791px">
      <svg width="322" height="371" viewBox="0 0 322 371" role="img" aria-label="Photo of ventilation ducting">
        <polygon points="161,0 322,93 322,278 161,371 0,278 0,93" fill="#6a6d70"/>
        <g fill="none" stroke="#fff" stroke-width="3">
          <circle cx="161" cy="145" r="7"/>
          <path d="M158 138c-6-14-2-26 10-26s14 14 4 26"/>
          <path d="M168 145c14-6 26-2 26 10s-14 14-26 4"/>
          <path d="M164 152c6 14 2 26-10 26s-14-14-4-26"/>
          <path d="M154 145c-14 6-26 2-26-10s14-14 26-4"/>
        </g>
      </svg>
      <div class="service-label">AIR TREATMENT</div>
    </div>
  </section>

  <section class="appointment">
    <div class="appointment-photo" role="img" aria-label="Outdoor air conditioning condenser beside a brick wall on green grass"></div>
    <div class="appointment-fade"></div>
    <h2 class="appointment-title">REQUEST AN APPOINTMENT</h2>
    <div class="form-field" style="top:137px">Name*</div>
    <div class="form-field" style="top:194px">E-mail*</div>
    <div class="form-field" style="top:252px">Telephone*</div>
    <div class="form-field message" style="top:310px">Write your message*</div>
    <a class="btn" href="#">Send</a>
  </section>

  <section class="contact">
    <h2 class="section-title contact-title">CONTACT US</h2>
    <ul class="contact-list">
      <li>
        <svg width="22" height="26" viewBox="0 0 24 28" style="left:-2px"><path fill="#2a9bc4" d="M12 0a10 10 0 0 0-10 10c0 7.5 10 18 10 18s10-10.5 10-18A10 10 0 0 0 12 0zm0 14a4 4 0 1 1 0-8 4 4 0 0 1 0 8z"/></svg>
        14 Rue des Ateliers Verts<br>69120 VAULX-LÈS-CLAIRS
      </li>
      <li>
        <svg width="20" height="20" viewBox="0 0 24 24"><path fill="#2a9bc4" d="M6.6 10.8a15 15 0 0 0 6.6 6.6l2.2-2.2a1 1 0 0 1 1-.25 11.4 11.4 0 0 0 3.6.57 1 1 0 0 1 1 1V20a1 1 0 0 1-1 1A17 17 0 0 1 3 4a1 1 0 0 1 1-1h3.5a1 1 0 0 1 1 1c0 1.25.2 2.45.57 3.57a1 1 0 0 1-.25 1z"/></svg>
        06 21 43 65 87<br>06 98 76 54 32
      </li>
      <li style="margin-top:44px">
        <svg width="22" height="16" viewBox="0 0 22 16"><rect width="22" height="16" rx="2" fill="#2a9bc4"/><path d="M1 2l10 7 10-7" fill="none" stroke="#fff" stroke-width="1.5"/></svg>
        contact@clarovent-services.fr
      </li>
    </ul>
    <div class="map" role="img" aria-label="Embedded street map showing the company location"></div>
  </section>

  <footer class="site-footer">
    <nav class="footer-nav">
      <a href="#">HOME</a>
      <a href="#">ABOUT</a>
      <a href="#">SERVICES</a>
      <a href="#">CONTACT US</a>
    </nav>
    <p class="copyright">© Copyright 2020 . ROLV . All Right Reserved</p>
    <div class="social" aria-label="Social links"><span></span><span></span><span></span></div>
  </footer>

</div>
</body>
</html>
```